Book Cover,

Our book is called "88 reasons nobody warns you about adulthood: Thriving Beyond Campus, Just one more Predictable Graduate Coping Manual.
The Cover art for our book is very vivid in our minds and we hope YOU can help us bring it to life!

Picture a college graduation, cap, gown, cameras stadium the whole nine yards. now focus on one college graduate a guy, long black hair, diploma in his had, facing the crowd, his parents, flashes going off around him, behind him, is the exit of the graduation ceremony, where his class mates are exiting, but its not an exit, its the edge of a massive cliff, and students are falling down, you see people mid air falling down, at the bottom of the cliff is a trampoline, where the kids are bouncing off,

the idea and theory behind the art is the moral of the book, the book is a satire on all post college survival guides, (and god only knows how many horrible ones are out there). This is to make fun of them shed some light on the situation and really give good clear advice. so the art needs to be fun cartoonish feel and really scream satire.

Please dont hesitate to ask us for more direction, but we hope this is a great start!
Updates

Reason: We have not found something that we are set on please send us more submissions!

Reason: We have seen things we like but arent sold on any one yet- as well we have both been out of the country and have not had time to seriously consider all the submissions thank you

Target Market(s)

17-25

Industry/Entity Type

College

Requirements
Must have
• lots of colors, we want the art to be very vibrant, also a pencil look, we want the art to look like it was drawn onto the book
Should not have
• should not look digital it needs to have a real art feel to it.

```html
<!DOCTYPE html>
<html lang="en">
<head>
<meta charset="utf-8">
<title>88 reasons nobody warns you about adulthood — Book Cover</title>
<link rel="stylesheet" href="https://fonts.googleapis.com/css2?family=Didact+Gothic&family=Montserrat:wght@700&display=swap">
<style>
  :root {
    --cover-red: #e0353c;
    --cover-crimson: #8e0f1c;
    --cover-wine: #b3162a;
    --cover-orange: #f06a1e;
    --cover-amber: #f59a3a;
    --cover-pink: #f48a98;
    --ink-maroon: #7a0d16;
    --ink-rust: #a3200f;
    --ink-red: #e21d28;
    --ink-orange: #e8501a;
    --ink-pink: #e44a5a;
    --paper: #ffffff;
    --frame: #ffffff;
  }
  * { margin: 0; padding: 0; box-sizing: border-box; }
  html, body {
    width: 872px; height: 1200px; overflow: hidden;
    background: var(--frame);
  }
  .cover {
    position: relative;
    width: 872px; height: 1200px;
    overflow: hidden;
    background: var(--frame);
  }
  .cover-art {
    position: absolute; left: 17px; top: 17px; right: 16px; bottom: 18px;
    background:
      radial-gradient(circle at 12% 8%, var(--cover-pink) 0 5%, transparent 13%),
      radial-gradient(circle at 50% 6%, var(--cover-crimson) 0 6%, transparent 15%),
      radial-gradient(circle at 88% 12%, var(--cover-wine) 0 7%, transparent 17%),
      radial-gradient(circle at 8% 30%, var(--cover-wine) 0 5%, transparent 13%),
      radial-gradient(circle at 30% 28%, var(--cover-crimson) 0 5%, transparent 12%),
      radial-gradient(circle at 92% 34%, var(--cover-crimson) 0 6%, transparent 15%),
      radial-gradient(circle at 8% 56%, var(--cover-orange) 0 7%, transparent 17%),
      radial-gradient(circle at 45% 50%, var(--cover-amber) 0 4%, transparent 12%),
      radial-gradient(circle at 80% 60%, var(--cover-pink) 0 4%, transparent 12%),
      radial-gradient(circle at 10% 80%, var(--cover-crimson) 0 5%, transparent 13%),
      radial-gradient(circle at 62% 78%, var(--cover-orange) 0 6%, transparent 15%),
      radial-gradient(circle at 90% 88%, var(--cover-wine) 0 7%, transparent 17%),
      radial-gradient(circle at 35% 95%, var(--cover-orange) 0 5%, transparent 13%),
      var(--cover-red);
  }
  .hands { position: absolute; inset: 0; }
  .hands path { fill: var(--paper); }
  .title { font-weight: normal; }
  .title-line {
    position: absolute;
    white-space: nowrap;
    line-height: 1;
    font-family: "Didact Gothic", sans-serif;
  }
  .bold { font-family: "Montserrat", sans-serif; font-weight: 700; }
  .number    { left: 430px; top: 200px; font-size: 122px; color: var(--ink-maroon); letter-spacing: -3px; }
  .reasons   { left: 382px; top: 318px; font-size: 50px; color: var(--ink-red); }
  .warns     { left: 440px; top: 388px; font-size: 58px; color: var(--ink-orange); }
  .warns .soft { font-family: "Didact Gothic", sans-serif; font-weight: 400; font-size: 42px; color: var(--ink-maroon); margin-left: 8px; position: relative; top: 20px; }
  .about     { left: 660px; top: 500px; font-size: 36px; color: var(--ink-maroon); }
  .adulthood { left: 580px; top: 556px; font-size: 46px; color: var(--ink-rust); }
  .thriving  { left: 134px; top: 724px; font-size: 46px; color: var(--ink-maroon); }
  .beyond    { left: 156px; top: 786px; font-size: 34px; color: var(--ink-maroon); }
  .just      { left: 110px; top: 846px; font-size: 48px; color: var(--ink-maroon); }
  .just .accent { color: var(--ink-red); }
  .predictable { left: 116px; top: 922px; font-size: 30px; color: var(--ink-rust); }
  .graduate  { left: 92px; top: 972px; font-size: 32px; color: var(--ink-pink); }
  .coping    { left: 48px; top: 1042px; font-size: 42px; color: var(--ink-orange); }
  .manual    { left: 38px; top: 1098px; font-size: 46px; color: var(--ink-maroon); }
  .byline {
    position: absolute; left: 566px; top: 1132px;
    font-family: "Montserrat", sans-serif; font-weight: 700;
    font-size: 30px; line-height: 1; color: var(--paper);
    display: flex; align-items: flex-end;
  }
  .byline .blank {
    display: inline-block; width: 196px; margin-left: 10px;
    border-bottom: 3px solid var(--paper);
  }
</style>
</head>
<body>
<main class="cover">
  <div class="cover-art" role="img" aria-label="Vivid red, orange and pink tie-dye burst pattern"></div>

  <svg class="hands" width="872" height="1200" viewBox="0 0 872 1200" role="img" aria-label="Two open white hands reaching toward each other">
    <path d="M270 110 C380 78 520 68 590 112 C670 170 770 330 856 430 L856 860 C760 790 640 680 540 570 C460 520 360 500 280 460 C215 420 195 340 212 270 C228 200 240 140 270 110 Z"/>
    <path d="M150 590 C260 552 420 556 520 626 C600 686 612 790 562 862 C500 942 380 962 320 1022 C270 1080 250 1140 240 1182 L17 1182 L17 1020 C60 980 82 920 92 840 C102 740 118 636 150 590 Z"/>
  </svg>

  <h1 class="title">
    <span class="title-line number bold">88</span>
    <span class="title-line reasons">reasons nobody</span>
    <span class="title-line warns bold">warns<span class="soft">you</span></span>
    <span class="title-line about bold">about</span>
    <span class="title-line adulthood bold">adulthood:</span>
    <span class="title-line thriving bold">Thriving</span>
    <span class="title-line beyond">Beyond Campus,</span>
    <span class="title-line just"><span class="bold accent">Just</span> one more</span>
    <span class="title-line predictable bold">Predictable</span>
    <span class="title-line graduate">Graduate</span>
    <span class="title-line coping bold">Coping</span>
    <span class="title-line manual bold">Manual.</span>
  </h1>

  <p class="byline">By,<span class="blank"></span></p>
</main>
</body>
</html>
```